PENNIMARTEL & PENNIMARTEL,LLP NEEDS A NEW LETTERHEAD DESIGN

a conservative yet contemporary layout befitting a long established
firm, consistent with the times, some form of logo so it catches ones attention, and is
admirable, but portrays integrity
Updates

I would like to approve #22066987 Please advise how to do this as it’s confusing on the site so I can approve payment for the designer

Target Market(s)

real estate investors and building management people

Industry/Entity Type

Law Firm

Font styles to use
Serif

Colors

Designer to choose colors to be used in the design.

Requirements
Must have
• some form of conservative logo

```html
<!DOCTYPE html>
<html lang="en">
<head>
<meta charset="UTF-8">
<title>Pennimartel &amp; Pennimartel, LLP — Letterhead</title>
<link rel="stylesheet" href="https://fonts.googleapis.com/css2?family=Montserrat:wght@500;600;700&display=swap">
<style>
  :root {
    --navy: #173a5e;
    --charcoal: #4b4d51;
    --mark-grey: #5a5c60;
    --paper: #f7f7f9;
    --ink: #2c2e33;
    --white: #ffffff;
  }
  * { margin: 0; padding: 0; box-sizing: border-box; }
  html, body { width: 891px; height: 1200px; overflow: hidden; background: var(--paper); }
  .letterhead {
    position: relative;
    width: 891px;
    height: 1200px;
    background: var(--paper);
    font-family: "Montserrat", Arial, sans-serif;
  }
  .header-band {
    position: absolute;
    top: 0;
    left: 120px;
    right: 0;
    height: 134px;
    background: var(--charcoal);
  }
  .header-mark {
    position: absolute;
    top: 8px;
    left: 48px;
    width: 118px;
    height: 118px;
    background: var(--navy);
    border: 5px solid var(--white);
  }
  .firm-name {
    position: absolute;
    top: 50px;
    left: 196px;
    color: var(--white);
    font-weight: 700;
    font-size: 27px;
    letter-spacing: 0.5px;
    white-space: nowrap;
  }
  .footer {
    position: absolute;
    left: 0;
    bottom: 0;
    width: 891px;
    height: 52px;
  }
  .footer-band {
    position: absolute;
    left: 0;
    top: 0;
    width: 385px;
    height: 52px;
    background: var(--navy);
  }
  .footer-name {
    position: absolute;
    left: 14px;
    top: 18px;
    color: var(--white);
    font-weight: 500;
    font-size: 13px;
    white-space: nowrap;
  }
  .footer-mark {
    position: absolute;
    left: 368px;
    top: 6px;
    width: 40px;
    height: 40px;
    background: var(--mark-grey);
    border: 3px solid var(--white);
  }
  .contact {
    position: absolute;
    top: 16px;
    display: flex;
    align-items: center;
    gap: 8px;
    color: var(--ink);
    font-weight: 600;
    font-size: 12px;
  }
  .contact-phone { left: 436px; }
  .contact-web { left: 590px; }
  .contact-icon {
    width: 20px;
    height: 20px;
    border-radius: 50%;
    background: var(--charcoal);
    display: flex;
    align-items: center;
    justify-content: center;
  }
</style>
</head>
<body>
  <main class="letterhead">
    <header>
      <div class="header-band"></div>
      <div class="header-mark" aria-hidden="true"></div>
      <h1 class="firm-name">PENNIMARTEL &amp; PENNIMARTEL,LLP</h1>
    </header>

    <footer class="footer">
      <div class="footer-band">
        <span class="footer-name">PENNIMARTEL &amp; PENNIMARTEL,LLP</span>
      </div>
      <div class="footer-mark" aria-hidden="true"></div>
      <div class="contact contact-phone">
        <span class="contact-icon">
          <svg width="11" height="11" viewBox="0 0 24 24" aria-hidden="true">
            <path fill="#fff" d="M6.6 10.8a15.1 15.1 0 0 0 6.6 6.6l2.2-2.2c.3-.3.7-.4 1-.2 1.1.4 2.3.6 3.6.6.6 0 1 .4 1 1V20c0 .6-.4 1-1 1A17 17 0 0 1 3 4c0-.6.4-1 1-1h3.5c.6 0 1 .4 1 1 0 1.3.2 2.5.6 3.6.1.3 0 .7-.2 1l-2.3 2.2z"/>
          </svg>
        </span>
        <span>0198765432</span>
      </div>
      <div class="contact contact-web">
        <span class="contact-icon">
          <svg width="12" height="12" viewBox="0 0 24 24" aria-hidden="true">
            <g fill="none" stroke="#fff" stroke-width="2">
              <circle cx="12" cy="12" r="9"/>
              <path d="M3 12h18M12 3c3 3 3 15 0 18M12 3c-3 3-3 15 0 18"/>
            </g>
          </svg>
        </span>
        <span>www.pennimartellaw.com</span>
      </div>
    </footer>
  </main>
</body>
</html>
```